QM Interiors needs and Interior Design Business card

I can do anything from Commercial to Residential and Free lance. Beginning to end in design selection process.
Need something to catch the eye of potential customers and vendors. From furniture to Tile and Cabinet selections. I can do it all.

Industry/Entity Type

Design Agency

Contact Information for Business Card

QM Interiors- Design Consultanting Residential, Commerical
Maybe a cool detail background. Wall paper print that can have some texture

Font styles to use
Serif

Colors
709dcb
34a6d7
b868aa
e667a6
f59296
85acd3
ffffff
000000
5c5c5c

Requirements
Must have
• Square or Rectangular with Rounded edges
• Name
• Address
• Phone
• Email
Nice to have
• Some colored edges More simples not too busy
• Pattern detail in background.
Should not have
• Not too much color

```html
<!DOCTYPE html>
<html lang="en">
<head>
<meta charset="utf-8">
<title>QM Interiors – Business Card</title>
<link href="https://fonts.googleapis.com/css2?family=Lora:wght@400;700&display=swap" rel="stylesheet">
<style>
  :root {
    --page: #e8e5e1;
    --paper: #f4f4f4;
    --ink: #1c1c1c;
    --black: #000000;
    --purple: #ab5ea1;
    --white: #ffffff;
    --grey: #5c5c5c;
  }
  * { box-sizing: border-box; margin: 0; padding: 0; }
  html, body {
    width: 1200px; height: 902px; overflow: hidden;
    background: var(--page);
  }
  .sheet { position: relative; width: 1200px; height: 902px; }
  .card {
    position: absolute; left: 250px; width: 700px; height: 400px;
    border-radius: 10px; overflow: hidden;
    background: var(--paper);
    box-shadow: 0 6px 18px rgba(0,0,0,.12);
  }
  .card--back { top: 40px; }
  .card--front { top: 462px; }

  .brand {
    position: absolute; display: flex; flex-direction: column; align-items: center;
    font-family: "Lora", serif; color: var(--ink);
  }
  .brand__circle { border: 4px solid var(--ink); border-radius: 50%; }
  .brand__name { letter-spacing: .16em; white-space: nowrap; font-weight: 400; }

  .card--back .brand { left: 0; right: 0; top: 78px; }
  .card--back .brand__circle { width: 150px; height: 150px; }
  .card--back .brand__name { font-size: 40px; margin-top: 34px; }

  .card__shapes { position: absolute; inset: 0; }

  .card--front .brand { left: 20px; width: 320px; top: 110px; }
  .card--front .brand__circle { width: 120px; height: 120px; }
  .card--front .brand__name { font-size: 28px; margin-top: 26px; }

  .person {
    position: absolute; right: 40px; top: 44px; text-align: right;
    font-family: "Lora", serif; color: var(--white);
  }
  .person__name { font-size: 34px; font-weight: 700; }
  .person__role { font-size: 20px; margin-top: 6px; }

  .contact {
    position: absolute; right: 28px; top: 206px; list-style: none;
    font-family: "Lora", serif; color: var(--white); font-size: 18px;
  }
  .contact__item {
    display: flex; justify-content: flex-end; align-items: center; gap: 12px;
    margin-bottom: 16px; white-space: nowrap;
  }
  .contact__icon { width: 18px; height: 18px; flex: none; }
</style>
</head>
<body>
<main class="sheet">

  <section class="card card--back" aria-label="Card back">
    <div class="brand">
      <div class="brand__circle"></div>
      <p class="brand__name">QM Interiors</p>
    </div>
  </section>

  <section class="card card--front" aria-label="Card front">
    <svg class="card__shapes" width="700" height="400" viewBox="0 0 700 400" aria-hidden="true">
      <rect width="700" height="400" fill="var(--purple)"/>
      <polygon points="226,0 700,0 700,168 368,168" fill="var(--black)"/>
      <polygon points="0,0 214,0 360,164 360,400 0,400" fill="var(--paper)"/>
      <rect x="360" y="162" width="7" height="238" fill="var(--black)"/>
    </svg>

    <div class="brand">
      <div class="brand__circle"></div>
      <p class="brand__name">QM Interiors</p>
    </div>

    <div class="person">
      <p class="person__name">Maren Holloway</p>
      <p class="person__role">Design Consultant</p>
    </div>

    <ul class="contact">
      <li class="contact__item">
        <span>021 5550 1482</span>
        <svg class="contact__icon" viewBox="0 0 18 18" aria-label="Phone">
          <rect width="18" height="18" rx="3" fill="var(--white)"/>
          <path d="M5 5 Q5 13 13 13 L13 11 L11 10 L10 11 Q7 10 7 8 L8 7 L7 5 Z" fill="var(--purple)"/>
        </svg>
      </li>
      <li class="contact__item">
        <span>studio@qminteriors.com</span>
        <svg class="contact__icon" viewBox="0 0 18 18" aria-label="Email">
          <rect width="18" height="18" rx="3" fill="var(--white)"/>
          <rect x="4" y="5.5" width="10" height="7" fill="none" stroke="var(--purple)" stroke-width="1.2"/>
          <path d="M4 5.5 L9 9.5 L14 5.5" fill="none" stroke="var(--purple)" stroke-width="1.2"/>
        </svg>
      </li>
      <li class="contact__item">
        <span>214 Alder Lane, Wellington</span>
        <svg class="contact__icon" viewBox="0 0 18 18" aria-label="Address">
          <rect width="18" height="18" rx="3" fill="var(--white)"/>
          <path d="M9 15 Q4.5 9.5 4.5 7.5 A4.5 4.5 0 0 1 13.5 7.5 Q13.5 9.5 9 15 Z" fill="var(--purple)"/>
          <circle cx="9" cy="7.5" r="1.6" fill="var(--white)"/>
        </svg>
      </li>
    </ul>
  </section>

</main>
</body>
</html>
```